Urban Music Nightclub DJ Flyer

The flyer is for a night at a San Diego bar called Velvet & Tide. We tend to play V&T that is more on the bassier side of things but still accessible to the ladies.

The flyer colors would be predominately in black and gold. We're going for a slightly sultry look.

- Ornate Gold frame around the picture.

Changes to the picture:

- Supplied photo has an undesirable tile background
- make it grayscale.

The fonts should complement the frame, have a bit of texture and depth.

Flyer should read

V&T (Largest font)
presents (smallest font)
T DELANO (Large Font)
FRAZOL x MONDRIK (smaller font)

We've included a quick mock up.

We thank you for the many designs that were submitted. We are close to making our final decision.

```html
<!DOCTYPE html>
<html lang="en">
<head>
<meta charset="utf-8">
<title>V&amp;T presents T Delano</title>
<link rel="stylesheet" href="https://fonts.googleapis.com/css2?family=Kreon:wght@400;600;700&display=swap">
<style>
  :root {
    --gold-deep: #b86f1f;
    --gold-mid: #e3962f;
    --gold-light: #f7b548;
    --gold-pale: #fcd37a;
    --ink: #000000;
    --headline: #f6be25;
    --accent-pink: #d9687a;
    --skin-tone: #b98a6e;
    --shirt-white: #e9e9e9;
  }
  html, body {
    margin: 0;
    padding: 0;
    width: 800px;
    height: 1200px;
    overflow: hidden;
    background: var(--ink);
  }
  .flyer {
    position: relative;
    width: 800px;
    height: 1200px;
    box-sizing: border-box;
    background:
      linear-gradient(135deg, var(--gold-deep) 0%, var(--gold-light) 22%, var(--gold-mid) 45%, var(--gold-deep) 60%, var(--gold-light) 82%, var(--gold-deep) 100%);
    font-family: "Kreon", Georgia, serif;
  }
  .frame-bevel {
    position: absolute;
    inset: 40px;
    background: linear-gradient(135deg, var(--gold-pale), var(--gold-deep) 50%, var(--gold-pale));
    box-shadow: inset 0 0 0 2px rgba(90, 50, 10, 0.55);
  }
  .stage {
    position: absolute;
    inset: 57px;
    background: var(--ink);
    overflow: hidden;
  }
  .portrait {
    position: absolute;
    left: 143px;
    top: 0;
    width: 420px;
    height: 650px;
  }
  .headline {
    position: absolute;
    left: 0;
    right: 0;
    top: 608px;
    margin: 0;
    text-align: center;
    font-weight: 700;
    font-size: 290px;
    line-height: 1;
    letter-spacing: 4px;
    color: var(--headline);
    text-shadow: 0 3px 0 rgba(120, 70, 10, 0.45);
  }
  .presents {
    position: absolute;
    left: 0;
    right: 0;
    top: 876px;
    margin: 0;
    text-align: center;
    font-size: 17px;
    font-weight: 400;
    color: var(--accent-pink);
  }
  .artist {
    position: absolute;
    left: 0;
    right: 0;
    top: 905px;
    margin: 0;
    text-align: center;
    font-size: 78px;
    font-weight: 700;
    letter-spacing: 3px;
    line-height: 1;
    color: var(--headline);
  }
  .support {
    position: absolute;
    left: 0;
    right: 0;
    top: 988px;
    margin: 0;
    text-align: center;
    font-size: 35px;
    font-weight: 600;
    letter-spacing: 2px;
    line-height: 1;
    color: var(--accent-pink);
  }
</style>
</head>
<body>
  <main class="flyer">
    <div class="frame-bevel"></div>
    <section class="stage">
      <svg class="portrait" viewBox="0 0 420 650" role="img" aria-label="Portrait photo of the headlining artist in a white tank top, arms raised above her head, fading into black">
        <defs>
          <linearGradient id="portrait-tone" x1="0" y1="0" x2="0" y2="1">
            <stop offset="0" stop-color="var(--skin-tone)"/>
            <stop offset="0.5" stop-color="var(--skin-tone)"/>
            <stop offset="0.6" stop-color="var(--shirt-white)"/>
            <stop offset="0.88" stop-color="var(--shirt-white)"/>
            <stop offset="1" stop-color="var(--ink)"/>
          </linearGradient>
          <linearGradient id="portrait-fade" x1="0" y1="0" x2="1" y2="0">
            <stop offset="0" stop-color="#000" stop-opacity="0.9"/>
            <stop offset="0.2" stop-color="#000" stop-opacity="0"/>
            <stop offset="0.8" stop-color="#000" stop-opacity="0"/>
            <stop offset="1" stop-color="#000" stop-opacity="0.9"/>
          </linearGradient>
        </defs>
        <rect x="0" y="0" width="420" height="650" fill="url(#portrait-tone)"/>
        <rect x="0" y="0" width="420" height="650" fill="url(#portrait-fade)"/>
      </svg>
      <h1 class="headline">V&amp;T</h1>
      <p class="presents">presents</p>
      <h2 class="artist">T DELANO</h2>
      <p class="support">FRAZOL &amp; MONDRIK</p>
    </section>
  </main>
</body>
</html>
```